Bright Harbour Charity - helping the disadvantaged

I would like a new web site design for my charity BRIGHT HARBOUR. The charity provides help for the disadvantaged. See current site
brightharbour.org.au for details. Please refer to the current site for information on the charity. The objectives of the charity are in the "about us" tab. You will also notice on the site that we provide information about events that we sponsor an area for this should be provided on the site.

Target Market(s)

We have two targets:
1. Individuals and Businesses that will donate money to the charity.
2. Individuals that are in need of support from the charity.

Industry/Entity Type

Charity

Requirements
Must have
• Ability for individuals to be able to understand the type of support we can provide.
Nice to have
• Our logo should be prominate on each pages
Should not have
• Should be use modern fonts

```html
<!DOCTYPE html>
<html lang="en">
<head>
<meta charset="utf-8">
<title>Bright Harbour</title>
<link href="https://fonts.googleapis.com/css2?family=Roboto+Condensed:wght@300;400;700&family=Arimo:wght@400&family=Questrial&display=swap" rel="stylesheet">
<style>
:root{
  --backdrop:#e3e3de;
  --page:#ffffff;
  --olive:#878814;
  --hero-dark:#141a1d;
  --ink:#3a3a3a;
  --body-ink:#5a5148;
  --footer:#404040;
  --brand:#7d9a1c;
  --accent:#e8a917;
}
*{box-sizing:border-box;margin:0;padding:0}
html,body{width:949px;height:1200px;overflow:hidden}
body{background:var(--backdrop);font-family:"Arimo",Arial,sans-serif;position:relative}
.page{position:absolute;left:89px;top:0;width:768px;height:1200px;background:var(--page)}
.abs{position:absolute}

.brand{left:128px;top:22px;display:flex;align-items:center;gap:8px}
.brand-dot{width:14px;height:14px;border-radius:50%;background:var(--accent)}
.brand-name{font-family:"Roboto Condensed",sans-serif;font-weight:400;font-size:26px;color:var(--brand);letter-spacing:.5px}

.account{left:700px;top:32px;display:flex;gap:14px;font-size:12px;color:#222}
.account span{display:flex;align-items:center;gap:5px}

.main-nav{left:119px;top:76px;width:709px;height:30px;border-radius:3px;
  background:linear-gradient(#a9aa35,#7b7a10);display:flex;align-items:center}
.main-nav a{color:#fff;text-decoration:none;font-size:12px;height:100%;display:flex;align-items:center;justify-content:center}
.main-nav a.sep{border-right:1px solid rgba(255,255,255,.25)}

.hero{left:121px;top:114px;width:708px;height:224px;border-radius:4px;background:var(--hero-dark);overflow:hidden}
.hero-photo{position:absolute;left:0;top:0;width:300px;height:224px;background:linear-gradient(90deg,#5c5a58,#3a3a3a 70%,var(--hero-dark))}
.hero-text{position:absolute;left:297px;top:66px;font-family:"Questrial",sans-serif;font-size:23px;line-height:37px;color:#fff}
.slide-arrow{top:194px;width:28px;height:28px;background:#2d2d2d;border-radius:2px;box-shadow:0 2px 2px rgba(0,0,0,.35);display:flex;align-items:center;justify-content:center}

.cta{top:340px;height:58px;width:348px;border-radius:0 0 5px 5px;background:linear-gradient(#a5a632,#6f6e0d);
  display:flex;align-items:center;justify-content:center;gap:16px;color:#fff;
  font-family:"Roboto Condensed",sans-serif;font-weight:700;font-size:20px;letter-spacing:.5px}

.section-title{font-family:"Roboto Condensed",sans-serif;font-weight:400;font-size:20px;color:var(--ink)}
.body-text{font-size:9.6px;line-height:21.6px;color:var(--body-ink);letter-spacing:-.1px}
.services{list-style:none}
.services li{position:relative;padding-left:12px;font-size:9.6px;line-height:21.6px;color:var(--body-ink);letter-spacing:-.1px}
.services li::before{content:"";position:absolute;left:0;top:7px;border-left:5px solid #7b7a10;border-top:3.5px solid transparent;border-bottom:3.5px solid transparent}

.news-title{font-family:"Roboto Condensed",sans-serif;font-weight:300;font-size:15px;color:#444}
.news-image-dark{background:linear-gradient(#0a0a0a,#1a1a1a 60%,#3a3320)}
.news-image-light{background:linear-gradient(#f1c75a 0%,#8fb8c8 45%,#ffffff 46%,#ffffff 100%)}
.read-more{width:77px;height:21px;background:var(--olive);color:#fff;font-size:12px;display:flex;align-items:center;justify-content:center}

.footer{left:89px;top:1121px;width:768px;height:79px;background:var(--footer);color:#fff}
.footer-nav{position:absolute;top:18px;width:100%;text-align:center;font-size:11px}
.footer-nav span.bar{margin:0 9px}
.copyright{position:absolute;top:52px;width:100%;text-align:center;font-size:9px}
</style>
</head>
<body>
<div class="page"></div>

<header>
  <div class="abs brand"><span class="brand-dot"></span><span class="brand-name">BRIGHT HARBOUR</span></div>
  <div class="abs account">
    <span><svg width="9" height="11" viewBox="0 0 9 11"><rect x="0" y="5" width="9" height="6" fill="#222"/><path d="M2 5V3.2a2.5 2.5 0 0 1 5 0V5" fill="none" stroke="#222" stroke-width="1.5"/></svg>Login</span>
    <span><svg width="12" height="11" viewBox="0 0 12 11"><circle cx="5" cy="3" r="2.6" fill="#222"/><path d="M0 11c0-3.5 2-5 5-5s5 1.5 5 5z" fill="#222"/><path d="M9 2h3M10.5 .5v3" stroke="#222" stroke-width="1.2"/></svg>Register</span>
  </div>
  <nav class="abs main-nav">
    <a class="sep" style="width:64px">Home</a>
    <a class="sep" style="width:77px">About Us</a>
    <a style="width:66px">Donate</a>
    <a style="width:62px">Apply</a>
    <a style="width:66px">Pledge</a>
    <a style="width:78px">Nominate</a>
    <a style="width:72px">Events</a>
    <a style="width:84px">Contact Us</a>
    <a style="width:68px">Directors</a>
  </nav>
</header>

<section class="abs hero">
  <div class="hero-photo" role="img" aria-label="Photograph of a smiling young girl"></div>
  <p class="hero-text">We need your support to<br>accommodate, feed and educate!</p>
</section>
<div class="abs slide-arrow" style="left:85px"><svg width="10" height="12" viewBox="0 0 10 12"><path d="M8 1L3 6l5 5" fill="none" stroke="#fff" stroke-width="2.4"/></svg></div>
<div class="abs slide-arrow" style="left:834px"><svg width="10" height="12" viewBox="0 0 10 12"><path d="M2 1l5 5-5 5" fill="none" stroke="#fff" stroke-width="2.4"/></svg></div>

<a class="abs cta" style="left:118px">
  <svg width="30" height="28" viewBox="0 0 30 28"><circle cx="18" cy="16" r="8" fill="none" stroke="#fff" stroke-width="2"/><path d="M4 10h8M8 6v8" stroke="#fff" stroke-width="2"/></svg>DONATE NOW</a>
<a class="abs cta" style="left:484px">
  <svg width="34" height="32" viewBox="0 0 34 32"><path d="M17 14C10 9 8 6 8 4a4 4 0 0 1 9-1 4 4 0 0 1 9 1c0 2-2 5-9 10z" fill="#fff"/><path d="M2 20c6 0 10 4 15 4s9-2 13-5l2 3c-4 4-9 7-15 7S6 26 2 26z" fill="#fff"/></svg>APPLY FOR A HELP</a>

<section>
  <h2 class="abs section-title" style="left:124px;top:412px">ABOUT US</h2>
  <p class="abs body-text" style="left:124px;top:441px;width:425px">Lorem Ipsum is simply dummy text of the printing and typesetting industry. Lorem Ipsum has been the industry's standard dummy text ever since the 1500s, when an unknown printer took a galley of type and scrambled it to make a type specimen book. It has survived not only five centuries, but also the leap into electronic typesetting, remaining essentially unchanged. It was popularised in the 1960s with the release of Letraset sheets containing Lorem Ipsum passages, and more recently with desktop publishing software like</p>
</section>

<section>
  <h2 class="abs section-title" style="left:577px;top:412px">OUR SERVICES</h2>
  <ul class="abs services" style="left:577px;top:440px;width:250px">
    <li>Making loans to people in need</li>
    <li>Providing training and education to people in need</li>
    <li>providing accommodation for people in medical care &amp; their carers and families</li>
    <li>Providing food to people in need;</li>
    <li>Providing cash payments to people in need</li>
  </ul>
</section>

<section>
  <h2 class="abs section-title" style="left:124px;top:593px">ANNOUNCEMENTS</h2>
  <h3 class="abs news-title" style="left:125px;top:618px">Unity Day Information Sheet &amp; Booking Form</h3>
  <div class="abs news-image-dark" style="left:125px;top:646px;width:344px;height:112px" role="img" aria-label="Unity Day banner with a row of colourful paper-chain figures"></div>
  <p class="abs body-text" style="left:123px;top:772px;width:692px">Fernvale's Inaugural Unity Day Event 2012 Unity Celebration Day – “ALL TOGETHER” Date: Saturday 17th May 2012 Venue: Larchmont Centre, Ashby Lane, Millbrook. Time: 10am – 3pm &nbsp; Unity Day is celebrated around Australia in May each year. It's a day where all Australians</p>
  <div class="abs read-more" style="left:124px;top:821px">Read more</div>

  <h3 class="abs news-title" style="left:125px;top:863px">Unity Day Information Sheet &amp; Booking Form</h3>
  <div class="abs news-image-light" style="left:126px;top:893px;width:417px;height:99px" role="img" aria-label="Row of colourful paper-chain figures above a short event tagline"></div>
  <p class="abs body-text" style="left:123px;top:1016px;width:692px">Fernvale's Inaugural Unity Day Event 2012 Unity Celebration Day – “ALL TOGETHER” Date: Saturday 17th May 2012 Venue: Larchmont Centre, Ashby Lane, Millbrook. Time: 10am – 3pm &nbsp; Unity Day is celebrated around Australia in May each year. It's a day where all Australians</p>
  <div class="abs read-more" style="left:124px;top:1066px">Read more</div>
</section>

<footer class="abs footer">
  <nav class="footer-nav">Home<span class="bar">|</span>About Us<span class="bar">|</span>Donate<span class="bar">|</span>Apply<span class="bar">|</span>Pledge<span class="bar">|</span>Nominate<span class="bar">|</span>Events<span class="bar">|</span>Contact Us<span class="bar">|</span>Directors</nav>
  <p class="copyright">Copyright © 2012 Bright Harbour Proprietary Limited. All Rights Reserved.</p>
</footer>
</body>
</html>
```